Design business cards for musician - Saxophone - Logo available

Hi all,

I want to have a new business card. I'm a professional saxophone player. I already have a logo and want that one in my business cards.

The colours that i've used in my logo are:

Blue: #0EBBD9
Black: #000000

In the business cards you're free to use other colors

I want to have the following credentials:

Name
Email
Telephone number
Website

```html
<!DOCTYPE html>
<html lang="en">
<head>
<meta charset="UTF-8">
<title>Corvin – Business Card</title>
<link href="https://fonts.googleapis.com/css2?family=Lato:wght@400;700;900&display=swap" rel="stylesheet">
<style>
  :root {
    --brand-blue: #0EBBD9;
    --brand-black: #000000;
    --card-white: #ffffff;
    --stage: #3a3d42;
    --text-on-blue: #ffffff;
  }
  * { margin: 0; padding: 0; box-sizing: border-box; }
  html, body {
    width: 1200px; height: 900px; overflow: hidden;
    background: var(--stage);
    font-family: 'Lato', sans-serif;
  }
  .canvas { position: relative; width: 1200px; height: 900px; }

  .card {
    position: absolute;
    width: 600px; height: 343px;
    border-radius: 26px;
    background: var(--card-white);
    overflow: hidden;
  }
  .card--front { left: 300px; top: 70px; }
  .card--back  { left: 300px; top: 487px; }

  .brand {
    position: absolute;
    display: flex; align-items: center; gap: 14px;
  }
  .brand__dot {
    width: 26px; height: 26px; border-radius: 50%;
    background: var(--brand-blue);
  }
  .brand__name {
    font-weight: 400; font-size: 50px; letter-spacing: 3px;
    color: var(--brand-black);
  }
  .card--front .brand { left: 50%; top: 50%; transform: translate(-50%, -50%); }
  .card--back .brand { left: 48px; top: 150px; }
  .card--back .brand__name { font-size: 42px; }

  .back-shape { position: absolute; inset: 0; }

  .name-band {
    position: absolute; left: 345px; top: 22px;
    color: var(--text-on-blue);
  }
  .name-band__name { font-weight: 900; font-size: 20px; letter-spacing: 0.3px; }
  .name-band__title { font-weight: 400; font-size: 14px; margin-top: 1px; }

  .address {
    position: absolute; left: 385px; top: 118px;
    color: var(--text-on-blue);
    font-size: 13.5px; line-height: 1.45;
  }

  .contacts {
    position: absolute; left: 425px; top: 210px;
    list-style: none;
    color: var(--text-on-blue);
    font-size: 13.5px;
  }
  .contacts li { display: flex; align-items: center; gap: 7px; height: 19px; }
  .contacts svg { width: 12px; height: 12px; fill: var(--text-on-blue); }
</style>
</head>
<body>
<main class="canvas">

  <section class="card card--front">
    <div class="brand">
      <span class="brand__dot"></span>
      <span class="brand__name">Corvin</span>
    </div>
  </section>

  <section class="card card--back">
    <svg class="back-shape" viewBox="0 0 600 343" width="600" height="343">
      <path d="M270 0 L600 0 L600 343 L385 343 C345 270 340 150 270 0 Z" fill="var(--brand-blue)"/>
      <path d="M270 0 C340 150 345 270 385 343" fill="none" stroke="var(--brand-black)" stroke-width="9"/>
      <path d="M296 16 L600 16 L600 72 L330 72 L318 82 L318 60 Z" fill="var(--brand-black)"/>
    </svg>

    <div class="brand">
      <span class="brand__dot"></span>
      <span class="brand__name">Corvin</span>
    </div>

    <div class="name-band">
      <p class="name-band__name">THEO MARLOWE</p>
      <p class="name-band__title">Managing Director</p>
    </div>

    <p class="address">2180 Linden Grove Road,<br>Ashford, MI 48207</p>

    <ul class="contacts">
      <li>
        <svg viewBox="0 0 24 24"><path d="M6.6 10.8a15.1 15.1 0 0 0 6.6 6.6l2.2-2.2c.3-.3.7-.4 1-.2 1.1.4 2.3.6 3.6.6.6 0 1 .4 1 1V20c0 .6-.4 1-1 1A17 17 0 0 1 3 4c0-.6.4-1 1-1h3.5c.6 0 1 .4 1 1 0 1.3.2 2.5.6 3.6.1.3 0 .7-.2 1z"/></svg>
        <span>555 218 4470</span>
      </li>
      <li>
        <svg viewBox="0 0 24 24"><path d="M2 5h20v14H2z M3.5 6.5 12 13l8.5-6.5" fill="var(--text-on-blue)"/><path d="M3 6l9 7 9-7" fill="none" stroke="var(--brand-blue)" stroke-width="2"/></svg>
        <span>hello@corvinsax.com</span>
      </li>
      <li>
        <svg viewBox="0 0 24 24"><circle cx="12" cy="12" r="10"/><path d="M2 12h20M12 2c3 3 3 17 0 20M12 2c-3 3-3 17 0 20" fill="none" stroke="var(--brand-blue)" stroke-width="1.6"/></svg>
        <span>www.corvinsax.com</span>
      </li>
    </ul>
  </section>

</main>
</body>
</html>
```